Sationery for a dental office
Brisk Dental
Project: Sationery for a dental office
Sationery for a dental office - Health
Creative Brief
Professional
Dr Nuvela Pritch
XXXX- be provided later
briskdentalqz@mailnest.example
www.briskhomedental.example
The phone number, email address, website address and address fields need to be included but should all be able to be edited it the final versions of all the stationery. Along with business name: Brisk Dental also include slogan and tagline: tagline: Family, cosmetic & Implant Dentistry slogan: A healthy body begins with a healthy mouth
One version of the business card should have an appointment card layout on the back, which has section for day, date, time to be filled in. Another version: just logo, slogan and tagline on one side of the card and the other side having, doctor's name, address, phone number, website address, email address Again all these fields need to be easily edited in the final version.

```html
<!DOCTYPE html>
<html lang="en">
<head>
<meta charset="utf-8">
<title>Brisk Dental Stationery</title>
<link rel="stylesheet" href="https://fonts.googleapis.com/css2?family=Marcellus+SC&family=Open+Sans:wght@400;600&display=swap">
<style>
  :root {
    --stage: #e4e4e4;
    --card: #ffffff;
    --navy: #0e2f6b;
    --blue: #1f5fb0;
    --sky: #3d8fd6;
    --teal: #5fc3c9;
    --ink: #3b4250;
    --muted: #7c8592;
    --rule: #b9c0c9;
  }
  * { box-sizing: border-box; margin: 0; padding: 0; }
  html, body { width: 1200px; height: 271px; overflow: hidden; background: var(--stage); }
  body { position: relative; font-family: "Open Sans", Arial, sans-serif; color: var(--ink); }
  .card {
    position: absolute; top: 12px; height: 242px; background: var(--card);
    box-shadow: 0 2px 5px rgba(0,0,0,.25); overflow: hidden;
  }
  .card--contact { left: 7px; width: 384px; }
  .card--brand { left: 408px; width: 377px; background: linear-gradient(180deg, #ffffff 0%, #eef0f2 60%, #d9dde2 100%); }
  .card--appointment { left: 806px; width: 384px; }
  .card svg.backdrop { position: absolute; inset: 0; }

  .brand-name { font-family: "Marcellus SC", Georgia, serif; color: var(--blue); letter-spacing: 2px; }
  .tagline { font-size: 6.5px; color: var(--muted); }

  /* contact card */
  .doctor { position: absolute; right: 22px; top: 24px; text-align: right; color: #fff; }
  .doctor__name { font-size: 13px; line-height: 17px; }
  .doctor__title { font-size: 6.5px; line-height: 9px; opacity: .85; }
  .contact-brand { position: absolute; left: 24px; top: 100px; }
  .contact-brand__mark { position: absolute; left: 0; top: 0; width: 28px; height: 28px; border-radius: 50%; background: var(--blue); }
  .contact-brand .brand-name { position: absolute; left: 36px; top: 2px; font-size: 17px; white-space: nowrap; }
  .contact-brand .tagline { position: absolute; left: 38px; top: 24px; white-space: nowrap; }
  .address { position: absolute; left: 24px; top: 180px; font-size: 7px; line-height: 10px; color: var(--ink); font-style: normal; }
  .details { position: absolute; left: 168px; top: 178px; font-size: 7px; line-height: 11px; list-style: none; }
  .details li { display: flex; align-items: center; gap: 5px; }
  .details svg { width: 7px; height: 7px; fill: var(--blue); }

  /* brand card */
  .brand-center { position: absolute; left: 0; right: 0; top: 26px; text-align: center; }
  .brand-center__mark { width: 56px; height: 56px; border-radius: 50%; background: linear-gradient(135deg, var(--sky), var(--navy)); margin: 0 auto 8px; }
  .brand-center .brand-name { font-size: 27px; letter-spacing: 3px; }
  .brand-center .tagline { font-size: 7px; margin-top: 2px; }
  .brand-center .slogan { font-size: 7px; color: var(--muted); }
  .brand-decor { position: absolute; left: 14px; top: 150px; width: 84px; height: 84px; border-radius: 50%; background: linear-gradient(135deg, rgba(61,143,214,.55), rgba(14,47,107,.55)); }
  .web { position: absolute; right: 20px; bottom: 18px; font-size: 7px; color: var(--ink); display: flex; align-items: center; gap: 4px; }
  .web__dot { width: 7px; height: 7px; border-radius: 50%; background: var(--blue); }

  /* appointment card */
  .appt__title { position: absolute; right: 36px; top: 22px; font-size: 15px; font-weight: 400; color: var(--blue); }
  .appt__field { position: absolute; font-size: 7.5px; display: flex; align-items: flex-end; gap: 4px; }
  .appt__line { flex: 1; border-bottom: 1px solid var(--rule); height: 9px; }
  .appt__days { position: absolute; left: 34px; top: 145px; display: flex; gap: 12px; font-size: 7.5px; }
  .appt__days span { display: flex; align-items: center; gap: 4px; }
  .appt__days i { display: inline-block; width: 17px; height: 11px; border: 1px solid var(--rule); }
  .appt__note { position: absolute; left: 34px; top: 176px; font-size: 7px; color: var(--ink); }
</style>
</head>
<body>

<section class="card card--contact">
  <svg class="backdrop" width="384" height="242" viewBox="0 0 384 242">
    <defs>
      <linearGradient id="band" x1="0" y1="0" x2="1" y2="0">
        <stop offset="0" stop-color="#1f5fb0"/>
        <stop offset="1" stop-color="#0e2f6b"/>
      </linearGradient>
    </defs>
    <path d="M0 0H384V72C300 98 190 70 120 78 70 84 30 92 0 98Z" fill="url(#band)"/>
    <path d="M0 94C60 74 130 88 210 82 280 76 330 82 384 68" fill="none" stroke="#ffffff" stroke-width="4"/>
    <path d="M0 102C70 84 140 96 220 90 290 84 340 90 384 78" fill="none" stroke="#5fc3c9" stroke-width="2"/>
    <path d="M0 242V222C80 208 160 236 240 226 300 218 350 228 384 232V242Z" fill="#eef3f9"/>
  </svg>
  <div class="doctor">
    <p class="doctor__name">Dr Nuvela Pritch</p>
    <p class="doctor__title">Your Title</p>
  </div>
  <div class="contact-brand">
    <span class="contact-brand__mark"></span>
    <p class="brand-name">Brisk Dental</p>
    <p class="tagline">Family, Cosmetic &amp; Implant Dentistry</p>
  </div>
  <address class="address">
    1208 Larkfield Row<br>Unit 106<br>Brookvale QZ 00000
  </address>
  <ul class="details">
    <li><svg viewBox="0 0 10 10"><path d="M2 0h2l1 3-1.5 1a6 6 0 0 0 2.5 2.5L7 5l3 1v2a2 2 0 0 1-2 2A8 8 0 0 1 0 2a2 2 0 0 1 2-2z"/></svg>(555) 014-2290</li>
    <li><svg viewBox="0 0 10 10"><rect x="1" y="1" width="8" height="8"/></svg>(555) 014-2291</li>
    <li><svg viewBox="0 0 10 10"><path d="M0 2h10v6H0zM0 2l5 3 5-3" stroke="#fff" stroke-width=".8"/></svg>briskdentalqz@mailnest.example</li>
    <li><svg viewBox="0 0 10 10"><circle cx="5" cy="5" r="4.5"/></svg>www.briskhomedental.example</li>
  </ul>
</section>

<section class="card card--brand">
  <div class="brand-decor" role="img" aria-label="Large faint brand emblem placeholder"></div>
  <div class="brand-center">
    <div class="brand-center__mark"></div>
    <p class="brand-name">Brisk Dental</p>
    <p class="tagline">Family, Cosmetic &amp; Implant Dentistry</p>
    <p class="slogan">A healthy body begins with a healthy mouth</p>
  </div>
  <p class="web">www.briskhomedental.example</p>
</section>

<section class="card card--appointment">
  <h2 class="appt__title">Next Appointment</h2>
  <p class="appt__field" style="left:34px;right:30px;top:56px">Name:<span class="appt__line"></span></p>
  <p class="appt__field" style="left:34px;width:160px;top:80px">Date:<span class="appt__line"></span></p>
  <p class="appt__field" style="left:210px;right:30px;top:80px">Time:<span class="appt__line"></span>AM/PM</p>
  <div class="appt__days">
    <span>Mon<i></i></span><span>Tue<i></i></span><span>Wed<i></i></span>
    <span>Thu<i></i></span><span>Fri<i></i></span><span>Sat<i></i></span>
  </div>
  <p class="appt__note">If unable to keep appointment kindly give 48 hrs notice in Advance</p>
  <p class="web"><span class="web__dot"></span>www.briskhomedental.example</p>
</section>

</body>
</html>
```